Flyer/Poster design required for volunteer activities

We need a STRIKING A4 Poster/Flyer advertising our conservation volunteer program activities which are currently happening in the area. This poster is to advertise the program once people have arrived on the island or to locals. The program covers 5 months, May-September 2019 and is focused on conservation. I have attached the following:
- a flyer which was previously created (QMR Habitat Helpers 2019 sm)to advertise the program - would prefer it has a similar striking resemblance, but not essential
- A mock up document 'HHQMR On Island Poster_2019_v2' with text -Logos-Images

Target Market(s)

Everyone interested in Environmental Adventure/Hiking/Citizen Science

Industry/Entity Type

Tourism

Font styles to use
Sans Serif

Requirements
Must have
• -A travel conservation focus
• -Must use 'QMR-Background Image' as the background to the design
• -The info of where to get more information and the social media details must be prominent

```html
<!DOCTYPE html>
<html lang="en">
<head>
<meta charset="utf-8">
<title>Quinn Mara Reef Habitat Helpers 2019</title>
<link rel="stylesheet" href="https://fonts.googleapis.com/css2?family=Bebas+Neue&family=Source+Sans+3:wght@400;600;700&display=swap">
<style>
  :root {
    --navy: #22367c;
    --blue: #2a4f9e;
    --yellow: #f8dc1c;
    --white: #ffffff;
    --paper: #f3f5f7;
    --ocean: #1f7db6;
    --lagoon: #2aa3c4;
    --forest: #3c6a36;
    --night: #0d1912;
    --display: 'Bebas Neue', 'Oswald', sans-serif;
    --body: 'Source Sans 3', 'Myriad Pro', sans-serif;
  }
  * { box-sizing: border-box; margin: 0; padding: 0; }
  html, body { width: 890px; height: 1200px; overflow: hidden; background: var(--paper); }
  .poster { position: relative; width: 890px; height: 1200px; overflow: hidden; font-family: var(--body); color: var(--white); }

  .backdrop {
    position: absolute; inset: 0;
    background: linear-gradient(180deg,
      #ffffff 0%, #f2f5f8 17%, #c9d9e6 24%, #5c9ac7 30%,
      var(--ocean) 38%, var(--lagoon) 46%, #2d8aa8 55%,
      #4d7a4a 64%, var(--forest) 74%, #24402a 86%, var(--night) 100%);
  }

  .frame-top { position: absolute; left: 36px; top: 20px; width: 818px; height: 22px; background: var(--yellow); }
  .frame-side { position: absolute; top: 20px; width: 22px; height: 900px;
    background: linear-gradient(180deg, var(--yellow) 0%, var(--yellow) 70%, rgba(248,220,28,0) 100%); }
  .frame-side.left { left: 36px; }
  .frame-side.right { left: 832px; }

  .title { position: absolute; left: 80px; top: 62px; font-family: var(--display); color: var(--navy); font-size: 100px; line-height: 1; letter-spacing: 0.5px; white-space: nowrap; }
  .subtitle { position: absolute; left: 82px; top: 150px; font-family: var(--display); color: var(--blue); font-size: 50px; line-height: 1; letter-spacing: 2px; white-space: nowrap; }

  .badge { position: absolute; left: 656px; top: 58px; width: 154px; height: 154px; border-radius: 50%; border: 5px solid var(--navy); background: var(--white); display: flex; align-items: center; justify-content: center; text-align: center; font-family: var(--display); color: var(--navy); font-size: 27px; line-height: 1.05; }

  .season { position: absolute; left: 58px; top: 210px; width: 370px; height: 36px; }
  .season svg { position: absolute; inset: 0; }
  .season span { position: absolute; left: 22px; top: 3px; font-family: var(--display); color: var(--navy); font-size: 33px; line-height: 1; white-space: nowrap; }

  .tagline { position: absolute; left: 82px; top: 260px; font-weight: 700; color: var(--blue); font-size: 19.5px; line-height: 29px; text-transform: uppercase; }

  .photo { position: absolute; width: 142px; height: 142px; border-radius: 50%; border: 7px solid var(--yellow); }
  .month-tab { position: absolute; height: 27px; min-width: 145px; background: var(--navy); font-family: var(--display); font-size: 26px; line-height: 29px; padding: 0 10px; white-space: nowrap; }
  .feature { position: absolute; height: 24px; min-width: 215px; background: var(--yellow); color: #2b5fb2; font-size: 14.5px; line-height: 24px; padding: 0 9px; white-space: nowrap; }
  .details { position: absolute; font-size: 11.2px; font-weight: 700; line-height: 13px; }
  .details h3 { font-size: 11.2px; font-weight: 700; text-transform: uppercase; }
  .details li { list-style: none; }
  .details li::before { content: "• "; }
  .right .details, .right .month-tab, .right .feature { text-align: right; }

  .footer-rule { position: absolute; left: 37px; top: 1115px; width: 816px; height: 3px; background: var(--yellow); }
  .more-info { position: absolute; left: 0; width: 890px; top: 1128px; text-align: center; font-size: 17px; font-weight: 600; }
  .follow { position: absolute; left: 0; width: 890px; top: 1160px; display: flex; justify-content: center; align-items: center; gap: 12px; font-family: var(--display); font-size: 27px; letter-spacing: 0.5px; }
  .follow .dot { width: 18px; height: 18px; background: var(--yellow); }
</style>
</head>
<body>
<main class="poster">
  <div class="backdrop" role="img" aria-label="Aerial photo of the island lagoon, coral reef and forested mountains"></div>

  <div class="frame-top"></div>
  <div class="frame-side left"></div>
  <div class="frame-side right"></div>

  <h1 class="title">QUINN MARA REEF</h1>
  <h2 class="subtitle">HABITAT HELPERS</h2>

  <div class="badge">QMR<br>HABITAT<br>HELPERS</div>

  <div class="season">
    <svg width="370" height="36" viewBox="0 0 370 36"><polygon points="0,0 356,0 370,36 0,36" fill="#f8dc1c"/></svg>
    <span>MAY – SEPTEMBER 2019</span>
  </div>

  <p class="tagline">Be involved in protecting paradise<br>Join the QMR Habitat Helpers program 2019</p>

  <!-- May -->
  <section class="month">
    <div class="photo" style="left:87px;top:324px;background:radial-gradient(circle at 45% 40%, #9a8f80, #5d6b45 60%, #2f3a24);" role="img" aria-label="Photo of a grey seabird resting among plants"></div>
    <div class="month-tab" style="left:217px;top:331px;">MAY 2019</div>
    <div class="feature" style="left:222px;top:360px;">Feature Week: 19th – 26th May</div>
    <div class="details" style="left:222px;top:389px;width:560px;">
      <h3>Birds of Quinn Mara Reef</h3>
      <ul>
        <li>Ocean bird watching boat trips</li>
        <li>Guided tours of Woodhen and Currawong quarters</li>
        <li>Weekly lectures at the Quinn Mara Reef Museum</li>
        <li>Weekly screenings of documentaries on Bird and Island Conservation projects</li>
        <li>Self guided land bird survey tours</li>
      </ul>
    </div>
  </section>

  <!-- June -->
  <section class="month right">
    <div class="photo" style="left:665px;top:476px;background:radial-gradient(circle at 50% 45%, #2f6d9a, #163a5e 65%, #0b1f33);" role="img" aria-label="Photo of a snorkeller recording marine life underwater"></div>
    <div class="month-tab" style="right:200px;top:481px;min-width:162px;">JUNE 2019</div>
    <div class="feature" style="right:227px;top:510px;">Feature Week: 3rd – 9th June</div>
    <div class="details" style="right:238px;top:539px;width:560px;">
      <h3>Quinn Mara Reef Marine Park</h3>
      <ul>
        <li>Marine pest monitoring with marine park staff</li>
        <li>Marine plastic &amp; debris clean up activities</li>
        <li>Screenings of marine conservation documentaries at the museum</li>
        <li>Weekly lectures on Marine Life at the Quinn Mara Reef Museum</li>
        <li>Marine Activities with local operators</li>
      </ul>
    </div>
  </section>

  <!-- July -->
  <section class="month">
    <div class="photo" style="left:84px;top:635px;background:radial-gradient(circle at 50% 50%, #e2c2ae, #c89a84 55%, #6f5a4d);" role="img" aria-label="Photo of cupped hands holding a large island stick insect"></div>
    <div class="month-tab" style="left:217px;top:641px;">JULY 2019</div>
    <div class="feature" style="left:222px;top:669px;">Feature Week: 21st – 28th July</div>
    <div class="details" style="left:222px;top:698px;width:560px;">
      <h3>Invasive Species</h3>
      <ul>
        <li>Guided walks to learn about the weed eradication program</li>
        <li>Weekly lectures on plants of Quinn Mara Reef</li>
        <li>Weekly screenings of documentaries on plant and island conservation projects</li>
        <li>Guided walks to Mount Alder</li>
        <li>Local tour guides include commentaries on island plants</li>
      </ul>
    </div>
  </section>

  <!-- August -->
  <section class="month right">
    <div class="photo" style="left:665px;top:795px;background:radial-gradient(circle at 50% 45%, #9bb27a, #4f6e34 60%, #263a1b);" role="img" aria-label="Photo of a hiker walking through palm forest"></div>
    <div class="month-tab" style="right:200px;top:800px;min-width:162px;">AUGUST 2019</div>
    <div class="feature" style="right:227px;top:828px;">Feature Week: 11th – 19th August</div>
    <div class="details" style="right:238px;top:857px;width:560px;">
      <h3>Amazing Invertebrates</h3>
      <ul>
        <li>Guided night walks to learn about the island's invertebrates</li>
        <li>Weekly viewing and presentation of the Quinn Mara Reef Phasmid</li>
        <li>Weekly lectures on invertebrates of Quinn Mara Reef at the museum</li>
        <li>Weekly screenings of documentaries on island conservation projects</li>
      </ul>
    </div>
  </section>

  <!-- September -->
  <section class="month">
    <div class="photo" style="left:84px;top:945px;background:linear-gradient(180deg, #cfe0ee 0%, #8fb6d4 45%, #4f7d5a 75%, #34502f 100%);" role="img" aria-label="Photo of a hiker standing on a clifftop above the lagoon"></div>
    <div class="month-tab" style="left:217px;top:951px;">SEPTEMBER 2019</div>
    <div class="feature" style="left:222px;top:979px;">Feature Week: 1st – 8th September</div>
    <div class="details" style="left:222px;top:1007px;width:608px;">
      <h3>Protecting Paradise</h3>
      <ul>
        <li>Observational snorkel surveys with Marine Ecologists, to assess populations of Reef-banded Anemonefish and other unique fish species</li>
        <li>Guided snorkel and glass bottom boat tour to assess coral health within the Quinn Mara Reef Marine Park</li>
        <li>Guided walks to learn about the island's conservation history</li>
      </ul>
    </div>
  </section>

  <div class="footer-rule"></div>
  <p class="more-info">See the QMR visitor centre for more information about the QMR Habitat Helpers program for 2019</p>
  <p class="follow"><span>FOLLOW US!</span><span class="dot"></span><span>WWW.HHQMR.ORG/SOCIAL PHOTOS@HHQMR</span></p>
</main>
</body>
</html>
```